Business Card Design for Flood Rescue 360 - Property Restoration Professionals

I need a business card designed for Flood Rescue 360. We are a full-service property restoration solution. Providing water, fire, smoke & storm restoration as well as mold remediation and full remodel or reconstruction to homes and businesses across Dallas-Fort Worth, TX.
Target Market(s)
home and business owners with insurance covered property damage from water, fire or storm related damage
Industry/Entity Type
property restoration
Contact Information for Business Card
Marcus Pellow General Manager Cell: 214-555-0193 Office: 469-555-0148 email: Marcus@FloodRescue360.example services: Water, Fire, Mold, Reconstruction Tagline: Urgency for Your Water Emergency!
Look and feel
Each slider illustrates characteristics of the customer's brand and the style your logo design should communicate.

```html
<!DOCTYPE html>
<html lang="en">
<head>
<meta charset="utf-8">
<title>Flood Rescue 360 – Business Card</title>
<link href="https://fonts.googleapis.com/css2?family=Montserrat:wght@400;500;700&display=swap" rel="stylesheet">
<style>
  :root {
    --bg: #ecebe9;
    --brand-blue: #10a9e6;
    --ink: #111111;
    --card-white: #ffffff;
    --card-black: #171717;
    --muted: #4a4a4a;
  }
  * { box-sizing: border-box; margin: 0; padding: 0; }
  html, body { width: 1200px; height: 768px; overflow: hidden; }
  body {
    background: var(--bg);
    font-family: "Montserrat", Arial, sans-serif;
    position: relative;
  }
  .card {
    position: absolute;
    top: 224px;
    width: 560px;
    height: 320px;
    border-radius: 4px;
    box-shadow: 0 10px 30px rgba(0,0,0,0.18);
    overflow: hidden;
  }
  .card-front { left: 30px; background: var(--card-white); color: var(--ink); }
  .card-back { left: 610px; background: var(--card-black); }

  .person { position: absolute; left: 34px; top: 30px; }
  .person-name { color: var(--brand-blue); font-weight: 700; font-size: 24px; }
  .person-title { font-size: 13px; margin-top: 2px; padding-bottom: 6px; border-bottom: 1.5px solid var(--brand-blue); display: inline-block; }

  .brand-name {
    position: absolute;
    font-weight: 700;
    font-size: 30px;
    white-space: nowrap;
    line-height: 1.2;
  }
  .card-front .brand-name { right: 36px; top: 120px; color: var(--brand-blue); }
  .card-back .brand-name { left: 0; right: 0; top: 112px; text-align: center; color: var(--muted); }

  .contact { position: absolute; left: 34px; bottom: 72px; list-style: none; font-size: 13px; }
  .contact li { display: flex; align-items: center; gap: 10px; margin-top: 6px; }
  .contact svg { width: 14px; height: 14px; fill: var(--brand-blue); flex: none; }

  .services { position: absolute; right: 34px; bottom: 24px; text-align: center; }
  .services-heading { color: var(--brand-blue); font-weight: 700; font-size: 16px; display: inline-block; border-bottom: 1.5px solid var(--brand-blue); padding-bottom: 2px; }
  .services-list { font-size: 13px; font-weight: 500; margin-top: 8px; }
  .services-list .sep { color: var(--brand-blue); margin: 0 3px; }

  .tagline {
    position: absolute; left: 0; right: 0; top: 184px; text-align: center;
    color: var(--brand-blue); font-weight: 700; font-size: 17px; letter-spacing: 0.3px;
  }
</style>
</head>
<body>
  <section class="card card-front" aria-label="Business card front">
    <div class="person">
      <div class="person-name">Marcus Pellow</div>
      <div class="person-title">General Manager</div>
    </div>

    <div class="brand-name">Flood Rescue 360</div>

    <ul class="contact">
      <li>
        <svg viewBox="0 0 24 24" aria-hidden="true"><path d="M6.6 10.8a15.1 15.1 0 0 0 6.6 6.6l2.2-2.2a1 1 0 0 1 1-.25 11.4 11.4 0 0 0 3.6.57 1 1 0 0 1 1 1V20a1 1 0 0 1-1 1A17 17 0 0 1 3 4a1 1 0 0 1 1-1h3.5a1 1 0 0 1 1 1c0 1.25.2 2.45.57 3.57a1 1 0 0 1-.25 1z"/></svg>
        214-555-0193
      </li>
      <li>
        <svg viewBox="0 0 24 24" aria-hidden="true"><path d="M3 9c0-2 4-4 9-4s9 2 9 4v2h-4V9H7v2H3zM6 12h12l2 8H4zm6 2a2.5 2.5 0 1 0 0 5 2.5 2.5 0 0 0 0-5z"/></svg>
        469-555-0148
      </li>
      <li>
        <svg viewBox="0 0 24 24" aria-hidden="true"><path d="M2 5h20v14H2zm2 2v.5l8 5 8-5V7l-8 5z"/></svg>
        Marcus@FloodRescue360.example
      </li>
    </ul>

    <div class="services">
      <div class="services-heading">Our Services</div>
      <div class="services-list"><span class="sep">•</span>Water<span class="sep">•</span>Fire<span class="sep">•</span>Mold<span class="sep">•</span>Reconstruction</div>
    </div>
  </section>

  <section class="card card-back" aria-label="Business card back">
    <div class="brand-name">Flood Rescue 360</div>
    <p class="tagline">Urgency for Your Water Emergency!</p>
  </section>
</body>
</html>
```